Vantrelo App Homepage Design making customers feel in control of their spend

Hi,
We need a App Homepage design with a UI similar to the attached mock up on an Quorix 4. The app is intended to put customers in control of their usage and spend on their fixed phone, broadband, mobile, gas and electricity.

Please fee free to propose improvements to the background images, icons, colours, etc.

Any questions please let me know.

Thanks
Bertram

Target Market(s)

Consumer customers

Industry/Entity Type

Internet

Font styles to use
Sans Serif

Colors
3276b5
0255a3
85acd3
cfdeed
ffffff

Requirements
Must have
• Content in line with the guidelines in the attached mock up

```html
<!DOCTYPE html>
<html lang="en">
<head>
<meta charset="utf-8">
<title>Vantrelo App Homepage</title>
<link rel="stylesheet" href="https://fonts.googleapis.com/css2?family=Arimo:wght@400;700&display=swap">
<style>
  :root{
    --page:#f0f0f0;
    --navy:#0d2f66;
    --brand-blue:#0255a3;
    --mid-blue:#3276b5;
    --soft-blue:#85acd3;
    --pale-blue:#cfdeed;
    --white:#ffffff;
    --elec:#2257a8;
    --gas:#e12a40;
    --calls:#f39a0a;
    --fibre:#e0137e;
    --mobile:#99b316;
    --font:"Arimo", Arial, Helvetica, sans-serif;
  }
  *{box-sizing:border-box;margin:0;padding:0}
  html,body{width:1200px;height:1200px;overflow:hidden}
  body{background:var(--page);font-family:var(--font);position:relative;color:var(--navy)}
  .icon-defs{position:absolute;width:0;height:0;overflow:hidden}
  .screen{position:absolute;left:136px;top:74px;width:602px;height:1067px;overflow:hidden}
  .screen-backdrop{position:absolute;inset:0;background:
      radial-gradient(ellipse at 40% 45%, #c7d5ef 0%, #aabfe6 45%, #98aee0 100%)}
  .app-header{position:absolute;left:0;top:0;width:100%;height:86px;background:rgba(220,232,248,.85);display:flex;align-items:center;padding-left:28px}
  .brand{display:flex;align-items:center;gap:12px}
  .brand-dot{width:40px;height:40px;border-radius:50%;background:var(--mid-blue)}
  .brand-name{font-weight:700;font-size:34px;color:var(--navy)}
  .menu-button{position:absolute;right:18px;top:12px;width:74px;height:60px;background:var(--mid-blue);display:flex;flex-direction:column;justify-content:center;align-items:center;gap:8px}
  .menu-button span{display:block;width:46px;height:5px;background:var(--white);border-radius:3px}
  .greeting{position:absolute;left:27px;top:115px;width:547px;height:131px;background:var(--white);border-radius:18px;text-align:center;padding-top:34px}
  .greeting::before{content:"";position:absolute;left:-14px;bottom:0;width:30px;height:18px;background:var(--white);border-bottom-left-radius:30px 18px}
  .greeting h1{font-size:35px;font-weight:700;color:var(--navy);line-height:1}
  .greeting p{font-size:24px;margin-top:12px;color:var(--navy)}
  .support-icon{position:absolute;left:502px;top:286px}
  .chart{position:absolute;left:62px;top:288px}
  .chart-centre{position:absolute;left:162px;top:460px;width:280px;text-align:center}
  .chart-centre .label{font-size:29px;font-weight:700;line-height:1.3;color:var(--navy)}
  .chart-centre .total{font-size:52px;font-weight:700;margin-top:10px;color:var(--navy)}
  .legend-item{position:absolute;display:flex;gap:16px;white-space:nowrap}
  .legend-icon{width:46px;height:32px;border-radius:9px;display:flex;align-items:center;justify-content:center;color:var(--white)}
  .legend-icon svg{width:20px;height:20px}
  .legend-text strong{display:block;font-size:16px;font-weight:700;letter-spacing:.8px;color:var(--navy)}
  .legend-text span{display:block;font-size:15px;margin-top:6px;color:var(--navy)}
  .bill-bar{position:absolute;left:18px;top:953px;width:568px;height:105px;background:linear-gradient(90deg,#3c86d6,#3a78d3);border-radius:6px;color:var(--white);text-align:center;font-weight:700;font-size:24px;line-height:1.35;padding-top:20px}
  .brand-lockup{position:absolute;left:828px;top:592px;display:flex;align-items:center;gap:20px}
  .brand-lockup .brand-dot{width:80px;height:80px}
  .brand-lockup .brand-name{font-size:54px}
</style>
</head>
<body>
<svg class="icon-defs" aria-hidden="true">
  <defs>
    <symbol id="icon-phone" viewBox="0 0 24 24"><path fill="currentColor" d="M6.6 10.8c1.4 2.8 3.8 5.1 6.6 6.6l2.2-2.2c.3-.3.7-.4 1-.2 1.1.4 2.3.6 3.6.6.6 0 1 .4 1 1V20c0 .6-.4 1-1 1C10.6 21 3 13.4 3 4c0-.6.4-1 1-1h3.5c.6 0 1 .4 1 1 0 1.3.2 2.5.6 3.6.1.3 0 .7-.2 1z"/></symbol>
    <symbol id="icon-globe" viewBox="0 0 24 24"><g fill="none" stroke="currentColor" stroke-width="2"><circle cx="12" cy="12" r="9"/><ellipse cx="12" cy="12" rx="4" ry="9"/><path d="M3 12h18"/></g></symbol>
    <symbol id="icon-flame" viewBox="0 0 24 24"><path fill="currentColor" d="M12 2c1 4 5 6 5 11a5 5 0 0 1-10 0c0-2 1-3.5 2-4.5 0 2 1 3 2 3 0-4-1-6 1-9.5z"/></symbol>
    <symbol id="icon-bolt" viewBox="0 0 24 24"><path fill="currentColor" d="M14 2L4 14h6l-2 8 11-13h-6z"/></symbol>
    <symbol id="icon-mobile" viewBox="0 0 24 24"><rect x="7" y="2.5" width="10" height="19" rx="2" fill="none" stroke="currentColor" stroke-width="2"/><circle cx="12" cy="18" r="1.2" fill="currentColor"/></symbol>
  </defs>
</svg>

<main class="screen">
  <div class="screen-backdrop" role="img" aria-label="Soft blue-tinted background photo of a customer looking at her phone"></div>

  <header class="app-header">
    <div class="brand"><span class="brand-dot"></span><span class="brand-name">Vantrelo</span></div>
    <div class="menu-button" aria-label="Menu"><span></span><span></span><span></span></div>
  </header>

  <section class="greeting">
    <h1>Good Morning Sophie</h1>
    <p>Welcome to Vantrelo!</p>
  </section>

  <svg class="support-icon" width="78" height="78" viewBox="0 0 78 78" aria-label="24/7 support">
    <path d="M30 8 A29 29 0 1 1 62 58" fill="none" stroke="var(--brand-blue)" stroke-width="5" stroke-linecap="round"/>
    <use href="#icon-phone" x="0" y="6" width="66" height="66" style="color:var(--brand-blue)"/>
    <text x="32" y="40" font-family="Arimo, Arial, sans-serif" font-size="15" font-weight="700" fill="var(--brand-blue)">24/7</text>
  </svg>

  <svg class="chart" width="480" height="480" viewBox="-240 -240 480 480" aria-label="Spend breakdown chart">
    <circle r="240" fill="rgba(220,232,248,.6)"/>
    <circle r="150" fill="rgba(200,218,244,.7)"/>
    <g stroke="rgba(220,232,248,.9)" stroke-width="4">
      <path d="M0 -232 A232 232 0 0 1 215.1 87 L131.6 53.2 A142 142 0 0 0 0 -142Z" fill="var(--elec)"/>
      <path d="M215.1 87 A232 232 0 0 1 -200.9 116 L-123 71 A142 142 0 0 0 131.6 53.2Z" fill="var(--gas)"/>
      <path d="M-200.9 116 A232 232 0 0 1 -231.9 -8.1 L-141.9 -5 A142 142 0 0 0 -123 71Z" fill="var(--mobile)"/>
      <path d="M-231.9 -8.1 A232 232 0 0 1 -218 -79.3 L-133.4 -48.6 A142 142 0 0 0 -141.9 -5Z" fill="var(--fibre)"/>
      <path d="M-218 -79.3 A232 232 0 0 1 0 -232 L0 -142 A142 142 0 0 0 -133.4 -48.6Z" fill="var(--calls)"/>
    </g>
    <g style="color:var(--white)">
      <use href="#icon-phone" x="-134" y="-170" width="40" height="40"/>
      <use href="#icon-bolt" x="156" y="-74" width="46" height="46"/>
      <use href="#icon-globe" x="-210" y="-56" width="36" height="36"/>
      <use href="#icon-mobile" x="-208" y="30" width="40" height="40"/>
      <use href="#icon-flame" x="-18" y="174" width="44" height="44"/>
    </g>
  </svg>

  <div class="chart-centre">
    <div class="label">Your current<br>total charges</div>
    <div class="total">£68.39</div>
  </div>

  <div class="legend">
    <div class="legend-item" style="left:43px;top:808px"><span class="legend-icon" style="background:var(--calls)"><svg><use href="#icon-phone"/></svg></span><div class="legend-text"><strong>CALLS</strong><span>£ 00.0 (%)</span></div></div>
    <div class="legend-item" style="left:222px;top:808px"><span class="legend-icon" style="background:var(--fibre)"><svg><use href="#icon-globe"/></svg></span><div class="legend-text"><strong>FIBRE</strong><span>£ 00.0 (%)</span></div></div>
    <div class="legend-item" style="left:422px;top:808px"><span class="legend-icon" style="background:var(--gas)"><svg><use href="#icon-flame"/></svg></span><div class="legend-text"><strong>GAS</strong><span>£ 00.0 (%)</span></div></div>
    <div class="legend-item" style="left:43px;top:883px"><span class="legend-icon" style="background:var(--elec)"><svg><use href="#icon-bolt"/></svg></span><div class="legend-text"><strong>ELECTRICITY</strong><span>£ 00.0 (%)</span></div></div>
    <div class="legend-item" style="left:257px;top:883px"><span class="legend-icon" style="background:var(--mobile)"><svg><use href="#icon-mobile"/></svg></span><div class="legend-text"><strong>MOBILE</strong><span>£ 00.0 (%)</span></div></div>
  </div>

  <div class="bill-bar">Last bill: £75.76 on 9/12/2016<br>Allowance renews in 18 days</div>
</main>

<div class="brand-lockup"><span class="brand-dot"></span><span class="brand-name">Vantrelo</span></div>
</body>
</html>
```